BARRIER BANNER KTV

I am looking for a visual for a banner
3 meters long by 1 high.
In the same theme as the visual identity of the company.
As simple as possible without overloading

There must be the LOGO, the title VOLTARIS SERVICES TECHNIQUES

_________________________

I am looking for a visual for a banner (barrier banner)
3 meters long by 1 high.

AIR CONDITIONING HEATING VENTILATION
04 52 31 69 14

Font styles to use
Sans Serif

Colors
33b8a4
00a990
33a6d7
0493ce
3176b5
0355a3
ffffff

Requirements
Should not have
• No photo
No photo

```html
<!DOCTYPE html>
<html lang="fr">
<head>
<meta charset="utf-8">
<title>KTV – Barrier banner</title>
<link rel="stylesheet" href="https://fonts.googleapis.com/css2?family=Archivo:wght@700;800;900&display=swap">
<style>
  :root {
    --teal: #26b9a2;
    --teal-deep: #00a990;
    --azure: #0493ce;
    --navy: #0355a3;
    --slate: #2c3d4a;
    --white: #ffffff;
    --page: #ffffff;
    --edge: #e6e9ec;
  }
  * { margin: 0; padding: 0; box-sizing: border-box; }
  html, body {
    width: 1200px;
    height: 800px;
    overflow: hidden;
    background: var(--page);
    font-family: "Archivo", Arial, sans-serif;
  }
  .banner {
    position: absolute;
    left: 30px;
    top: 202px;
    width: 1140px;
    height: 395px;
    background: var(--white);
    overflow: hidden;
    box-shadow: 0 0 0 1px var(--edge);
  }
  .side-panel {
    position: absolute;
    top: 0;
    width: 170px;
    height: 100%;
  }
  .side-panel--left {
    left: 0;
    background: linear-gradient(160deg, var(--navy) 0%, var(--azure) 45%, var(--teal) 100%);
  }
  .side-panel--right {
    right: 0;
    background: linear-gradient(340deg, var(--navy) 0%, var(--azure) 45%, var(--teal) 100%);
  }
  .banner__content {
    position: absolute;
    left: 170px;
    right: 170px;
    top: 0;
    bottom: 0;
    text-align: center;
  }
  .brand-name {
    position: absolute;
    left: 0; right: 0;
    top: 18px;
    font-size: 150px;
    line-height: 1;
    font-weight: 900;
    letter-spacing: 4px;
    color: var(--slate);
  }
  .company-name {
    position: absolute;
    left: 0; right: 0;
    top: 176px;
    font-size: 29px;
    font-weight: 700;
    letter-spacing: 0.5px;
    color: var(--slate);
  }
  .services {
    position: absolute;
    left: 0; right: 0;
    top: 226px;
    font-size: 52px;
    line-height: 47px;
    font-weight: 900;
    color: var(--navy);
  }
  .phone {
    position: absolute;
    left: 0; right: 0;
    top: 334px;
    font-size: 42px;
    font-weight: 800;
    letter-spacing: 1px;
    color: var(--teal-deep);
  }
</style>
</head>
<body>
  <main class="banner">
    <div class="side-panel side-panel--left" role="img" aria-label="Geometric decoration in blue and teal tones"></div>
    <div class="side-panel side-panel--right" role="img" aria-label="Geometric decoration in blue and teal tones"></div>
    <div class="banner__content">
      <div class="brand-name">KTV</div>
      <div class="company-name">VOLTARIS SERVICES TECHNIQUES</div>
      <h1 class="services">AIR CONDITIONING<br>HEATING VENTILATION</h1>
      <div class="phone">04 52 31 69 14</div>
    </div>
  </main>
</body>
</html>
```